Postcard Design

www.tovil.com.au
i am an occupational therapist and professionally trained coach. i work with children, parents and disability service providers to achieve brilliant outcomes for children with special needs.
http://www.tovil.com.au/service/for-families
I need a postcard to give parents to promote our family service coaching service
A family service coach will work with you to set specific goals for your child, build a dream team, design and manage your child's highly effective therapy and educational team to ensure brilliant outcomes for your child..
KORBU - you have done my business card previously. they were great thank you.

```html
<!DOCTYPE html>
<html lang="en">
<head>
<meta charset="utf-8">
<title>Family Service Coaching – tovil postcard</title>
<link href="https://fonts.googleapis.com/css2?family=Arimo:ital,wght@0,400;0,700;1,400;1,700&display=swap" rel="stylesheet">
<style>
  :root {
    --backdrop: #4a4748;
    --paper: #ffffff;
    --brand-blue: #5b80b8;
    --brand-navy: #24408c;
    --ink: #2b2b2b;
    --contact-tint: #cdd8ee;
    --photo-warm: #d9c3a8;
    --photo-light: #eef1ee;
    --photo-blue: #6f8fb8;
  }
  * { margin: 0; padding: 0; box-sizing: border-box; }
  html, body {
    width: 1200px; height: 980px; overflow: hidden;
    background: var(--backdrop);
    font-family: "Arimo", Arial, sans-serif;
  }
  .postcard {
    position: absolute; left: 79px; top: 92px;
    width: 1042px; height: 801px;
    background: var(--paper); overflow: hidden;
  }
  .family-photo {
    position: absolute; left: 290px; top: 95px;
    width: 752px; height: 560px;
    background:
      radial-gradient(ellipse at 30% 45%, var(--photo-warm) 0%, transparent 45%),
      radial-gradient(ellipse at 75% 55%, var(--photo-blue) 0%, transparent 50%),
      linear-gradient(180deg, var(--photo-light) 0%, #e4dccf 60%, #b9b3ad 100%);
    -webkit-mask-image: linear-gradient(90deg, transparent 0%, #000 20%);
    mask-image: linear-gradient(90deg, transparent 0%, #000 20%);
  }
  .headline {
    position: absolute; left: 51px; top: 40px;
    font-size: 63px; font-weight: 400; letter-spacing: 0.5px;
    color: var(--brand-blue); line-height: 1;
  }
  .service-summary {
    position: absolute; left: 51px; top: 136px; width: 290px;
    font-size: 21px; font-style: italic; line-height: 25.5px;
    color: var(--ink);
  }
  .visit-label {
    position: absolute; left: 52px; top: 449px;
    font-size: 20px; font-weight: 700; font-style: italic;
    color: var(--brand-blue);
  }
  .website {
    position: absolute; left: 53px; top: 476px;
    font-size: 26px; color: var(--brand-blue);
  }
  .footer-wave { position: absolute; left: 0; top: 0; }
  .brand {
    position: absolute; left: 48px; top: 650px;
    display: flex; align-items: center; gap: 40px;
  }
  .brand-dot {
    width: 86px; height: 86px; border-radius: 50%;
    background: var(--paper);
  }
  .brand-name {
    font-size: 74px; font-weight: 700; color: var(--paper); line-height: 1;
  }
  .contact {
    position: absolute; left: 520px; top: 665px; width: 480px;
    text-align: center;
  }
  .contact-call {
    font-size: 27px; font-weight: 700; color: var(--paper);
  }
  .contact-phone {
    margin-top: 6px;
    display: flex; align-items: center; justify-content: center; gap: 14px;
    font-size: 46px; font-weight: 700; color: var(--contact-tint);
  }
  .contact-email {
    margin-top: 4px;
    display: flex; align-items: center; justify-content: center; gap: 14px;
    font-size: 27px; font-weight: 700; color: var(--contact-tint);
  }
</style>
</head>
<body>
  <main class="postcard">
    <div class="family-photo" role="img" aria-label="Photo of smiling parents with a toddler and baby meeting a family service coach at home"></div>

    <h1 class="headline">FAMILY SERVICE COACHING</h1>

    <p class="service-summary">A family service coach will work with you to set specific goals for your child, build a dream team, design and manage your child's highly effective therapy and educational team to ensure brilliant outcomes for your child..</p>

    <p class="visit-label">VIST US TODAY</p>
    <p class="website">www.tovil.com.au</p>

    <svg class="footer-wave" width="1042" height="801" viewBox="0 0 1042 801" aria-hidden="true">
      <path d="M0,575 C200,505 430,515 640,560 C830,600 960,625 1042,590 L1042,801 L0,801 Z" fill="var(--brand-navy)"/>
      <path d="M0,600 C210,545 430,550 640,590 C830,625 960,640 1042,605 L1042,801 L0,801 Z" fill="var(--paper)"/>
      <path d="M0,606 C210,552 430,557 640,597 C830,632 960,648 1042,612 L1042,801 L0,801 Z" fill="var(--brand-blue)"/>
    </svg>

    <div class="brand">
      <span class="brand-dot"></span>
      <span class="brand-name">tovil</span>
    </div>

    <section class="contact">
      <p class="contact-call">Make your Appointment Today!</p>
      <p class="contact-phone">
        <svg width="34" height="40" viewBox="0 0 34 40" aria-hidden="true">
          <ellipse cx="17" cy="20" rx="15" ry="18" fill="none" stroke="var(--contact-tint)" stroke-width="2"/>
          <path d="M12,10 C8,14 8,26 12,30 L15,27 C13,24 13,16 15,13 Z" fill="var(--contact-tint)"/>
        </svg>
        0491 570 227
      </p>
      <p class="contact-email">
        <svg width="26" height="18" viewBox="0 0 26 18" aria-hidden="true">
          <rect x="1" y="1" width="24" height="16" fill="none" stroke="var(--contact-tint)" stroke-width="1.5"/>
          <path d="M1,1 L13,10 L25,1 M1,17 L10,8 M25,17 L16,8" fill="none" stroke="var(--contact-tint)" stroke-width="1.5"/>
        </svg>
        anna@tovil.com.au
      </p>
    </section>
  </main>
</body>
</html>
```